Workforce Equity Lens Poster for staff

Our organization has developed an equity lens to be used by staff when implementing new programs and services. We need a poster that will be used as a quick reference for staff to use on a daily basis and will hang in cubicles. We'd like the main six questions to stand out with the subsequent questions less prominent. Looking for a poster that is 11 x 17 inches.

Industry/Entity Type

Equity

Font styles to use
Sans Serif

Colors

Designer to choose colors to be used in the design.

Requirements
Must have
• Easy to read. Not too text heavy, so any way to highlight the main six questions. It would be great to have some sort of icon or illustration with each of the six questions.
Nice to have
• Illustrative design features.
Should not have
• No photos of people.

```html
<!DOCTYPE html>
<html lang="en">
<head>
<meta charset="utf-8">
<title>Ridgeway County Workforce System Equity Lens</title>
<link rel="stylesheet" href="https://fonts.googleapis.com/css2?family=Montserrat:wght@500;600;700&family=Arimo:wght@400&display=swap">
<style>
  :root {
    --page: #eeeeec;
    --poster: #9aae44;
    --band: #7f993a;
    --stripe: #a4b94d;
    --ink: #ffffff;
    --ink-soft: rgba(255,255,255,0.88);
    --rule: rgba(255,255,255,0.55);
  }
  * { box-sizing: border-box; margin: 0; padding: 0; }
  html, body { width: 1152px; height: 1200px; overflow: hidden; background: var(--page); }
  .poster {
    position: absolute; left: 176px; top: 30px; width: 800px; height: 1140px;
    background: var(--poster); color: var(--ink);
    font-family: "Arimo", Arial, sans-serif;
    overflow: hidden;
  }
  .brand {
    position: absolute; top: 52px; left: 0; right: 0;
    display: flex; justify-content: center; align-items: center; gap: 14px;
  }
  .brand-mark { width: 40px; height: 40px; border-radius: 50%; background: var(--ink); }
  .brand-name {
    font-family: "Montserrat", sans-serif; font-weight: 700; font-size: 24px;
    line-height: 1.05; letter-spacing: 0.5px;
  }
  .brand-name span { display: block; font-size: 13px; letter-spacing: 9px; }
  .lens-title {
    position: absolute; top: 134px; left: 0; right: 0; height: 44px;
    border-top: 1px solid var(--rule); border-bottom: 1px solid var(--rule);
    display: flex; align-items: center; justify-content: center;
    font-family: "Montserrat", sans-serif; font-weight: 500; font-size: 17px; letter-spacing: 5px;
  }
  .questions { position: absolute; top: 180px; left: 0; right: 0; }
  .q-row {
    position: absolute; left: 0; right: 0; background: var(--band);
    display: flex; align-items: flex-start; padding: 10px 40px 0 82px;
  }
  .q-row::before, .q-row::after {
    content: ""; position: absolute; left: 0; right: 0; height: 12px; background: var(--stripe);
  }
  .q-row::before { top: -22px; }
  .q-row::after { bottom: -22px; }
  .q-icon { position: absolute; left: 84px; top: 14px; width: 26px; height: 26px; }
  .q-body { margin-left: 52px; }
  .q-heading {
    font-family: "Montserrat", sans-serif; font-weight: 600; font-size: 19px;
    letter-spacing: 2.4px; text-transform: uppercase; line-height: 1.2;
  }
  .q-detail {
    margin-top: 8px; font-size: 9px; letter-spacing: 0.9px; line-height: 1.3;
    text-transform: uppercase; color: var(--ink-soft);
  }
  .about {
    position: absolute; top: 856px; left: 0; right: 0; height: 227px;
    border-top: 1px solid var(--rule);
  }
  .about-col { position: absolute; top: 30px; }
  .about-col h2 {
    font-family: "Montserrat", sans-serif; font-weight: 600; font-size: 15px; letter-spacing: 2px;
    margin-bottom: 7px;
  }
  .about-col p {
    font-size: 7.8px; line-height: 1.15; letter-spacing: 0.3px; text-transform: uppercase;
    color: var(--ink-soft);
  }
  .about-col p + p { margin-top: 9px; }
  .equity { left: 70px; width: 228px; text-align: right; }
  .lens { left: 353px; width: 412px; }
  .divider { position: absolute; left: 325px; top: 22px; width: 1px; height: 180px; background: var(--rule); }
  .foot-rule { position: absolute; left: 0; right: 0; top: 1083px; height: 1px; background: var(--rule); }
</style>
</head>
<body>
<main class="poster">
  <header class="brand">
    <div class="brand-mark"></div>
    <div class="brand-name">RIDGEWAY WORKFORCE<span>PARTNERSHIP</span></div>
  </header>
  <h1 class="lens-title">RIDGEWAY COUNTY WORKFORCE SYSTEM EQUITY LENS</h1>

  <section class="questions">
    <article class="q-row" style="top:32px;height:76px;">
      <svg class="q-icon" viewBox="0 0 26 26" fill="none" stroke="#fff" stroke-width="1.5"><circle cx="11" cy="11" r="8"/><line x1="17" y1="17" x2="24" y2="24"/></svg>
      <div class="q-body">
        <h2 class="q-heading">Who is affected?</h2>
        <p class="q-detail">Who are the groups affected by this policy, metric, program, decision, or proposed action?<br>How will each group be affected? Is any group negatively affected in a disproportionate<br>way?</p>
      </div>
    </article>
    <article class="q-row" style="top:133px;height:76px;">
      <svg class="q-icon" viewBox="0 0 26 26" fill="none" stroke="#fff" stroke-width="1.5"><path d="M15 4H3v19h19V11"/><path d="M10 16l1-4 11-10 3 3-11 10z"/></svg>
      <div class="q-body">
        <h2 class="q-heading">Are they at the table?</h2>
        <p class="q-detail">How have you actively involved stakeholders who are also members of the communities<br>affected by the policy, metric, program, decision, or proposed action?</p>
      </div>
    </article>
    <article class="q-row" style="top:234px;height:76px;">
      <svg class="q-icon" viewBox="0 0 26 26" fill="none" stroke="#fff" stroke-width="1.5"><path d="M4 25V4h18l-4 5 4 5H4"/></svg>
      <div class="q-body">
        <h2 class="q-heading">What are the barriers?</h2>
        <p class="q-detail">What are the societal or organizational barriers that prevent a population from being<br>successful?</p>
      </div>
    </article>
    <article class="q-row" style="top:335px;height:76px;">
      <svg class="q-icon" viewBox="0 0 26 26" fill="none" stroke="#fff" stroke-width="1.5"><path d="M2 20c2-7 8-10 15-10V5l8 7-8 7v-5c-6 0-10 2-15 6z"/></svg>
      <div class="q-body">
        <h2 class="q-heading">What are population-specific strategies?</h2>
        <p class="q-detail">To address any inequities, do we have solutions that are tailored to work for the<br>disproportionately affected groups? Have we used the ‘platinum rule’?</p>
      </div>
    </article>
    <article class="q-row" style="top:436px;height:76px;">
      <svg class="q-icon" viewBox="0 0 26 26" fill="none" stroke="#fff" stroke-width="1.5"><circle cx="13" cy="13" r="11.5"/><line x1="13" y1="11" x2="13" y2="19"/><circle cx="13" cy="7.5" r="0.8" fill="#fff"/></svg>
      <div class="q-body">
        <h2 class="q-heading">Are there unintended consequences?</h2>
        <p class="q-detail">Does this policy, program, decision, or proposed action ignore or worsen existing<br>disparities or produce other unintended consequences?</p>
      </div>
    </article>
    <article class="q-row" style="top:537px;height:103px;">
      <svg class="q-icon" viewBox="0 0 26 26" fill="none" stroke="#fff" stroke-width="1.5"><rect x="1" y="3" width="20" height="16"/><rect x="5" y="7" width="20" height="16"/></svg>
      <div class="q-body">
        <h2 class="q-heading">How do we measure success in a<br>population-specific way?</h2>
        <p class="q-detail" style="margin-top:6px;">Describe how data about the policy, metric, program, decision, or proposed action, and its<br>impact (positive or negative) on equitable access and outcomes, will be monitored and<br>evaluated?</p>
      </div>
    </article>
  </section>

  <section class="about">
    <div class="about-col equity">
      <h2>WHAT IS EQUITY?</h2>
      <p>In workforce development, equity is the notion that everyone has the opportunity to obtain quality, living wage employment or be placed in employment-related training regardless of their national origin, race, gender, sexual orientation, disability, first language or other distinguishing characteristic. Different approaches to delivery of workforce services may be necessary in order for each customer to achieve success in training or employment.</p>
    </div>
    <div class="divider"></div>
    <div class="about-col lens">
      <h2>WHAT IS AN EQUITY LENS?</h2>
      <p>An equity lens is a practical tool that will help ensure that policies, programs, decisions, or proposed actions in Ridgeway County's workforce system result in equitable outcomes for all job seekers. This lens shall be used by the Ridgeway Workforce Partnership Board of Directors when making policy decisions or decisions on how to allocate funding. It shall also be used by Ridgeway Workforce Partnership staff, WorkPath Ridgeway staff, and other workforce system partners when creating and implementing programs.</p>
      <p>The purpose of the equity lens is to provide a tool to assist the board and staff with identifying potentially negative outcomes for policies, programs, decisions, or actions that could increase disparities for under-represented populations. An equity lens is not meant to block to effectively delivering workforce services, but rather a mechanism to identify and remove systemic barriers for under-represented populations as it relates to workforce-related services.</p>
    </div>
  </section>
  <div class="foot-rule"></div>
</main>
</body>
</html>
```